Presentation Flyer for Married Couple at night separate business owners by day

I would like a flyer to use to advertise free presentations put on by husband and I. I (Danielle Vorhagen) am an estate planning attorney that works for PMR Law. My husband (Ray Vorhagen) is a financial planner that works for Belvorne Financial Planning. Would love it to be funny but serious. At night we are a married couple of 4 children, by day we individually work with people helping them protect their assets and their families.
Goal is for this to be used for multiple events.
Things to include: Food will be provided, Raffle for $500 off an Estate Plan Package
Topics to be covered in Seminar:
Estate & Financial Planning Essentials

Protect Your Future
Build a strong financial foundation with emergency funds, retirement planning, and smart investment strategies that match your goals.

Secure Your Legacy
Learn about wills, trusts, and powers of attorney - the essential documents everyone needs to protect their family's future.

Guard Your Assets
Understand the right insurance coverage to protect yourself and your loved ones, from life insurance to long-term care options.

Transfer Wealth Wisely
Discover tax-efficient strategies for passing assets to the next generation and making the most of your charitable giving.

```html
<!DOCTYPE html>
<html lang="en">
<head>
<meta charset="UTF-8">
<title>Married by Night – Free Estate &amp; Financial Planning Seminar</title>
<link href="https://fonts.googleapis.com/css2?family=Cinzel:wght@600;700;800&family=Poppins:wght@400;500;600;700&display=swap" rel="stylesheet">
<style>
  :root{
    --teal:#1b7271;
    --teal-bright:#23908d;
    --blue:#0b3f86;
    --link-blue:#1d5aa8;
    --white:#ffffff;
    --text-dark:#0b0b0b;
  }
  *{margin:0;padding:0;box-sizing:border-box}
  html,body{width:990px;height:1200px;overflow:hidden;background:#a3a3a3}
  .flyer{
    position:relative;width:990px;height:1200px;overflow:hidden;
    background:
      radial-gradient(ellipse 70% 55% at 75% 20%, #1b2f55 0%, rgba(20,38,72,0) 70%),
      linear-gradient(180deg,#0e1f3d 0%,#0a1730 45%,#050a14 80%,#020408 100%);
    font-family:'Poppins',sans-serif;color:var(--white);
  }
  .display{font-family:'Cinzel',serif;font-weight:700;line-height:1;text-transform:uppercase;white-space:nowrap}
  .tag{
    position:absolute;left:82px;width:210px;height:36px;
    background:var(--teal);border-radius:0 18px 18px 0;
    border-left:4px solid var(--teal-bright);
    font-family:'Cinzel',serif;font-weight:800;font-size:25px;letter-spacing:1.5px;
    text-transform:uppercase;
    padding-left:18px;line-height:36px;color:var(--white);
  }
  .tag--night{top:57px}
  .tag--day{top:235px}
  .headline{position:absolute;left:80px}
  .headline--married{top:106px;font-size:56px;color:var(--teal)}
  .headline--couple{top:168px;font-size:58px;color:var(--white)}
  .headline--your{top:289px;font-size:32px;color:var(--white)}
  .headline--estate{top:326px;font-size:56px;color:var(--teal);line-height:1.05}
  .headline--experts{top:445px;font-size:31px;color:var(--white)}

  .offer{position:absolute;left:539px;top:58px;display:flex;height:95px}
  .offer__free{
    width:174px;background:var(--teal);border-radius:12px 0 0 12px;
    text-align:center;padding-top:10px;
  }
  .offer__free .big{font-family:'Cinzel',serif;font-weight:800;font-size:46px;line-height:1}
  .offer__free .small{font-weight:600;font-size:29px;line-height:1.1}
  .offer__extras{
    width:150px;background:var(--white);color:var(--text-dark);border-radius:0 12px 12px 0;
    font-size:12px;font-weight:600;line-height:1.25;padding:13px 12px;
  }
  .intro{
    position:absolute;left:543px;top:182px;width:350px;
    border-left:2px solid var(--teal);padding-left:13px;
    font-size:15.3px;line-height:1.22;
  }
  .intro strong{font-weight:700}

  .portrait{
    position:absolute;left:470px;top:360px;width:520px;height:690px;
    background:
      radial-gradient(ellipse 45% 55% at 78% 45%, rgba(40,52,78,.9) 0%, rgba(40,52,78,0) 70%),
      radial-gradient(ellipse 40% 55% at 38% 55%, rgba(38,40,54,.95) 0%, rgba(38,40,54,0) 70%),
      linear-gradient(180deg,rgba(5,10,20,0) 0%,rgba(5,10,20,0) 75%,#04080f 100%);
  }

  .topics-label{
    position:absolute;left:82px;top:1004px;width:457px;
    transform:rotate(-90deg);transform-origin:0 0;
    font-family:'Cinzel',serif;font-weight:600;font-size:33px;letter-spacing:4px;
    text-transform:uppercase;white-space:nowrap;line-height:28px;
  }
  .topic{
    position:absolute;width:155px;border-radius:10px;
    text-align:center;padding:27px 12px 0;
  }
  .topic--teal{background:var(--teal)}
  .topic--blue{background:var(--blue)}
  .topic__tick{position:absolute;left:50%;top:-14px;margin-left:-14px;width:28px;height:28px}
  .topic__title{font-family:'Cinzel',serif;font-weight:700;font-size:12.5px;line-height:1.15;margin-bottom:8px;text-transform:uppercase}
  .topic__text{font-size:12.2px;line-height:1.2}
  .t1{left:129px;top:556px;height:198px}
  .t2{left:294px;top:556px;height:198px}
  .t3{left:129px;top:794px;height:199px}
  .t4{left:294px;top:794px;height:199px}

  .reserve{
    position:absolute;left:62px;top:1065px;font-family:'Cinzel',serif;font-weight:800;font-size:21px;
    text-transform:uppercase;color:var(--teal-bright);
  }
  .reserve span{color:var(--link-blue)}
  .links{position:absolute;left:60px;top:1102px;font-size:16.5px;letter-spacing:2.3px;line-height:24px}
  .links li{list-style:none;display:flex;align-items:center;gap:6px}
  .links svg{width:14px;height:14px}

  .firm-name{
    position:absolute;top:1080px;
    font-family:'Cinzel',serif;font-weight:700;color:var(--white);
    text-align:center;white-space:nowrap;text-transform:uppercase;
  }
  .firm-name--law{left:481px;width:260px;font-size:36px}
  .firm-name--finance{left:763px;width:170px;top:1086px;font-size:28px}
</style>
</head>
<body>
<main class="flyer">
  <div class="tag tag--night">By Night</div>
  <h1>
    <span class="headline headline--married display">A Married</span>
    <span class="headline headline--couple display">Couple</span>
    <span class="tag tag--day">By Day</span>
    <span class="headline headline--your display">Your</span>
    <span class="headline headline--estate display">Estate &amp;<br>Financial</span>
    <span class="headline headline--experts display">Planning Experts</span>
  </h1>

  <div class="offer">
    <div class="offer__free"><div class="big">FREE</div><div class="small">Seminar</div></div>
    <div class="offer__extras">Food Provided<br>+<br>Raffle for $500 Off an Estate Plan Package!</div>
  </div>

  <p class="intro"><strong>Danielle Vorhagen, Estate Planning Attorney at PMR Law,</strong> and <strong>Ray Vorhagen, Financial Planner at Belvorne Financial Planning,</strong> for an informative (and slightly entertaining) evening designed to help you protect your future, secure your legacy, and guard your assets.</p>

  <div class="portrait" role="img" aria-label="Portrait photo of the married couple, smiling, seated together in business attire"></div>

  <div class="topics-label">Topics We'll Cover</div>

  <section class="topic topic--teal t1">
    <svg class="topic__tick" viewBox="0 0 28 28"><circle cx="14" cy="14" r="13" fill="#fff"/><path d="M9 14.5l3.3 3.2L19 11" stroke="#0c1b35" stroke-width="2.6" fill="none" stroke-linecap="round" stroke-linejoin="round"/></svg>
    <h2 class="topic__title">Protect Your Future</h2>
    <p class="topic__text">Build a strong financial foundation with emergency funds, retirement planning, and smart investment strategies that match your goals.</p>
  </section>
  <section class="topic topic--blue t2">
    <svg class="topic__tick" viewBox="0 0 28 28"><circle cx="14" cy="14" r="13" fill="#fff"/><path d="M9 14.5l3.3 3.2L19 11" stroke="#0c1b35" stroke-width="2.6" fill="none" stroke-linecap="round" stroke-linejoin="round"/></svg>
    <h2 class="topic__title">Secure Your Legacy</h2>
    <p class="topic__text">Learn about wills, trusts, and powers of attorney - the essential documents everyone needs to protect their family's future.</p>
  </section>
  <section class="topic topic--blue t3">
    <svg class="topic__tick" viewBox="0 0 28 28"><circle cx="14" cy="14" r="13" fill="#fff"/><path d="M9 14.5l3.3 3.2L19 11" stroke="#0c1b35" stroke-width="2.6" fill="none" stroke-linecap="round" stroke-linejoin="round"/></svg>
    <h2 class="topic__title">Guard Your Assets</h2>
    <p class="topic__text">Understand the right insurance coverage to protect yourself and your loved ones, from life insurance to long-term care options.</p>
  </section>
  <section class="topic topic--teal t4">
    <svg class="topic__tick" viewBox="0 0 28 28"><circle cx="14" cy="14" r="13" fill="#fff"/><path d="M9 14.5l3.3 3.2L19 11" stroke="#0c1b35" stroke-width="2.6" fill="none" stroke-linecap="round" stroke-linejoin="round"/></svg>
    <h2 class="topic__title">Transfer Wealth Wisely</h2>
    <p class="topic__text">Discover tax-efficient strategies for passing assets to the next generation and making the most of your charitable giving.</p>
  </section>

  <div class="reserve">Reserve Your <span>Spot Today</span></div>
  <ul class="links">
    <li><svg viewBox="0 0 14 14"><circle cx="7" cy="7" r="6" fill="none" stroke="#1d5aa8" stroke-width="1.4"/><path d="M1 7h12M7 1c-3 3.5-3 8.5 0 12M7 1c3 3.5 3 8.5 0 12" fill="none" stroke="#1d5aa8" stroke-width="1"/></svg>www.guardandgrowwealth.com</li>
    <li><svg viewBox="0 0 14 14"><circle cx="7" cy="7" r="6" fill="none" stroke="#1d5aa8" stroke-width="1.4"/><path d="M1 7h12M7 1c-3 3.5-3 8.5 0 12M7 1c3 3.5 3 8.5 0 12" fill="none" stroke="#1d5aa8" stroke-width="1"/></svg>www.pmrlawgroup.com</li>
  </ul>

  <div class="firm-name firm-name--law">PMR Law</div>
  <div class="firm-name firm-name--finance">Belvorne</div>
</main>
</body>
</html>
```